Staffing Services Company Needs a New Site

View www.lorvanix.com for the current website. New logo is attached. We need this in a wordpress ready site. Additional details will be coming shortly.

Industry/Entity Type

It Company

Number of Pages Required

1 page

```html
<!DOCTYPE html>
<html lang="en">
<head>
<meta charset="utf-8">
<title>Lorvanix — Network and Exchange Gateway</title>
<link href="https://fonts.googleapis.com/css2?family=Open+Sans:wght@300;400;600;700&display=swap" rel="stylesheet">
<style>
:root{
  --navy:#1f3a82;
  --navy-dark:#16285c;
  --green:#3d9b35;
  --green-dark:#2f7d29;
  --text:#444;
  --muted:#777;
  --line:#dcdcdc;
  --band:#efefef;
  --footer:#2b2b2b;
  --footer-dark:#1e1e1e;
  --red:#c8312b;
}
*{box-sizing:border-box;margin:0;padding:0}
html,body{width:1200px;height:3000px;overflow:hidden}
body{font-family:"Open Sans",Arial,sans-serif;color:var(--text);background:#fff;font-size:12px;line-height:1.5}
.wrap{width:960px;margin:0 auto;position:relative}
.photo{background:linear-gradient(135deg,#5c7ea6,#aebfd2);}
.btn{display:inline-block;background:var(--green);color:#fff;font-size:10px;font-weight:600;padding:4px 12px;border-radius:2px}

/* header */
.site-header{height:104px;border-bottom:4px solid var(--navy)}
.site-header .wrap{height:100px}
.brand{position:absolute;left:0;top:18px;display:flex;align-items:center;gap:10px}
.brand-mark{width:40px;height:40px;background:var(--green)}
.brand-name{font-size:30px;font-weight:700;color:var(--navy)}
.login{position:absolute;right:0;top:0;background:var(--navy);color:#fff;font-size:10px;padding:2px 12px}
.phone{position:absolute;right:260px;top:22px;display:flex;align-items:center;gap:8px;font-size:22px;font-weight:700;color:var(--navy)}
.search{position:absolute;right:0;top:24px;width:240px;height:26px;border:1px solid var(--line);font-size:11px;color:#999;padding:4px 8px}
.search svg{position:absolute;right:6px;top:5px}
.main-nav{position:absolute;right:0;top:66px;background:var(--navy);display:flex}
.main-nav a{color:#fff;font-size:12px;padding:7px 11px;text-decoration:none}

/* slider */
.hero{margin-top:14px;height:380px;position:relative;background:linear-gradient(120deg,#2c3e5c,#8fa3bc 55%,#dfe6ee)}
.hero-caption{position:absolute;left:110px;right:110px;bottom:40px;background:rgba(20,30,60,.55);padding:10px 16px;color:#fff}
.hero-caption h2{font-size:21px;font-weight:600;text-transform:uppercase}
.hero-caption p{font-size:11px}
.arrow{position:absolute;top:170px;width:30px;height:30px;border-radius:50%;background:rgba(120,120,120,.8)}
.arrow.left{left:10px}.arrow.right{right:10px}
.dots{display:flex;gap:5px;justify-content:center;margin-top:10px}
.dots span{width:9px;height:9px;border-radius:50%;background:#999}
.dots span:first-child{background:var(--red)}

/* intro */
.tagline{text-align:center;margin:34px 0 26px;font-size:22px;font-weight:300;color:#333;text-transform:uppercase;line-height:1.3}
.features{display:flex;justify-content:space-between;border-top:1px solid var(--line);padding-top:14px}
.feature{width:290px;text-align:center}
.feature h3{font-size:16px;font-weight:400;text-transform:uppercase;color:#333;margin-bottom:10px}
.feature .icon{width:56px;height:56px;border-radius:50%;background:var(--navy);margin:0 auto 12px;display:flex;align-items:center;justify-content:center}
.feature p{text-align:left;font-size:11px;color:var(--muted);margin-bottom:10px}
.feature .btn{float:left}

/* welcome */
.split{display:flex;justify-content:space-between;margin-top:60px}
.welcome{width:620px}
.welcome h2{font-size:22px;font-weight:400;color:#333;margin-bottom:12px}
.welcome h2 span{color:var(--navy)}
.welcome p{font-size:11px;color:var(--muted);margin-bottom:12px}
.welcome .btn{float:right}
.gallery{width:300px;border:1px solid var(--line)}
.panel-title{background:var(--navy);color:#fff;font-size:11px;font-weight:600;text-transform:uppercase;padding:6px 10px}
.gallery-grid{display:grid;grid-template-columns:repeat(3,1fr);gap:6px;padding:8px}
.gallery-grid div{height:82px}
.view-all{text-align:right;font-size:10px;color:var(--red);padding:0 8px 6px}

/* blog */
.section-title{font-size:12px;font-weight:700;text-transform:uppercase;color:#333;border-bottom:1px solid var(--line);padding-bottom:6px;margin-bottom:10px}
.blog{width:620px}
.post{display:flex;gap:10px;padding:6px 0;border-bottom:1px solid #eee}
.post .thumb{width:70px;height:44px;flex:none}
.post h4{font-size:11px;font-weight:600;color:#333}
.post p{font-size:10px;color:var(--muted)}
.more{text-align:right;font-size:10px;color:var(--red);margin-top:6px}
.events{width:300px}
.event{display:flex;gap:8px;padding:6px 0;border-bottom:1px solid #eee}
.event .thumb{width:46px;height:46px;flex:none}
.event h4{font-size:10px;font-weight:600;color:var(--navy)}
.event p{font-size:9px;color:var(--muted)}

/* projects */
.projects{margin-top:44px}
.project-row{display:flex;justify-content:space-between}
.project{width:228px;text-align:center}
.project .photo{height:130px}
.project h4{font-size:12px;font-weight:400;color:#333;margin-top:8px}
.project p{font-size:10px;color:var(--muted)}

/* testimonials */
.testimonials{background:var(--band);margin-top:44px;padding:24px 0;height:230px}
.quote{width:600px}
.quote h3{font-size:14px;font-weight:600;color:#333;margin-bottom:10px}
.quote p{font-size:13px;font-weight:600;color:#333;line-height:1.4}
.quote .who{font-size:10px;font-weight:400;color:var(--muted);margin-top:8px}
.newsletter{position:absolute;right:0;top:-8px;width:300px;background:var(--navy);color:#fff;padding:0 0 14px}
.newsletter .panel-title{background:var(--navy-dark)}
.newsletter p{text-align:center;font-size:11px;margin:12px 16px}
.newsletter .field{display:flex;margin:0 16px}
.newsletter .field span{flex:1;background:#fff;height:24px;color:#999;font-size:10px;padding:4px 8px}
.newsletter .field b{background:var(--green);font-size:10px;padding:5px 10px}
.newsletter .check{font-size:9px;margin:8px 16px 0;display:flex;gap:6px;align-items:center}
.newsletter .check i{width:10px;height:10px;background:#fff;display:block}

/* about */
.about{display:flex;gap:26px;margin-top:40px}
.about .photo{width:270px;height:170px;flex:none}
.about h2{font-size:22px;font-weight:400;color:#333;margin-bottom:10px}
.about p{font-size:11px;color:var(--muted);margin-bottom:10px}
.about .btn{float:right}

/* partners */
.partners{display:flex;justify-content:space-between;align-items:center;margin-top:34px;border-top:1px solid var(--line);padding-top:24px}
.partners span{width:90px;height:40px;background:#d7dbe2;border-radius:3px}

/* footer */
.site-footer{position:absolute;left:0;top:2576px;width:1200px;height:424px;background:var(--footer);color:#bbb}
.footer-cols{display:flex;justify-content:space-between;padding-top:24px}
.footer-col h5{color:#fff;font-size:11px;text-transform:uppercase;margin-bottom:10px;border-bottom:1px solid #444;padding-bottom:5px}
.footer-col li{list-style:none;font-size:11px;line-height:1.9}
.menu-col{width:150px}
.links-col{width:160px}
.tweets-col{width:300px}
.tweet{display:flex;gap:8px;margin-bottom:10px;font-size:10px}
.tweet i{width:12px;height:12px;background:#1f88c9;flex:none;display:block;margin-top:2px}
.socials{display:flex;gap:8px;margin-top:8px}
.socials span{width:26px;height:26px;border-radius:50%;background:#fff}
.contact-col{width:260px}
.form-row{display:flex;align-items:center;margin-bottom:8px;font-size:10px}
.form-row label{width:64px}
.form-row span{flex:1;height:20px;background:#fff}
.form-row.msg span{height:70px}
.submit{float:right;background:#fff;color:#333;font-size:10px;padding:3px 10px}
.footer-bar{position:absolute;left:0;bottom:0;width:1200px;height:70px;background:var(--footer-dark);text-align:center}
.footer-brand{display:inline-flex;align-items:center;gap:8px;margin-top:10px;background:#fff;padding:3px 12px}
.footer-brand i{width:18px;height:18px;background:var(--green);display:block}
.footer-brand b{font-size:16px;color:var(--navy)}
.copyright{font-size:10px;color:#999;margin-top:6px}
</style>
</head>
<body>

<header class="site-header">
  <div class="wrap">
    <div class="brand"><span class="brand-mark"></span><span class="brand-name">Lorvanix</span></div>
    <div class="login">LOGIN</div>
    <div class="phone">
      <svg width="20" height="20" viewBox="0 0 24 24"><path d="M6.6 10.8a15 15 0 0 0 6.6 6.6l2.2-2.2c.3-.3.7-.4 1-.2 1.1.4 2.3.6 3.6.6.6 0 1 .4 1 1V20c0 .6-.4 1-1 1A17 17 0 0 1 3 4c0-.6.4-1 1-1h3.5c.6 0 1 .4 1 1 0 1.3.2 2.5.6 3.6.1.3 0 .7-.2 1z" fill="#1f3a82"/></svg>
      1 - 555 - 014 - 2290
    </div>
    <div class="search">Search<svg width="14" height="14" viewBox="0 0 24 24"><circle cx="10" cy="10" r="6" stroke="#1f3a82" stroke-width="2.5" fill="none"/><path d="M15 15l6 6" stroke="#1f3a82" stroke-width="2.5"/></svg></div>
    <nav class="main-nav">
      <a>Home</a><a>About Us</a><a>Services</a><a>News</a><a>Blog</a><a>Testimonials</a><a>Apply</a><a>Contact</a>
    </nav>
  </div>
</header>

<main class="wrap">
  <section class="hero" role="img" aria-label="Two IT technicians working beside server racks in a data centre">
    <span class="arrow left"></span><span class="arrow right"></span>
    <div class="hero-caption">
      <h2>Lorem ipsum dolor sit amet consectetur adipiscing elit</h2>
      <p>Sed do eiusmod tempor incididunt ut labore et dolore magna aliqua ut enim ad minim veniam quis.</p>
    </div>
  </section>
  <div class="dots"><span></span><span></span><span></span><span></span></div>

  <h2 class="tagline">We are network and exchange gateway with over 4,000<br>service professionals</h2>

  <section class="features">
    <div class="feature">
      <h3>Who we are</h3>
      <div class="icon"><svg width="28" height="28" viewBox="0 0 24 24" fill="#fff"><circle cx="8" cy="8" r="3"/><circle cx="16" cy="8" r="3"/><path d="M2 19c0-3 3-5 6-5s6 2 6 5z"/><path d="M10 19c0-3 3-5 6-5s6 2 6 5z"/></svg></div>
      <p>Lorem ipsum dolor sit amet, consectetur adipiscing elit. Sed vitae lacus. Nulla porttitor pellentesque nulla in vehicula. Aliquam erat volutpat. Etiam sollicitudin tellus a molestie.</p>
      <span class="btn">Read more</span>
    </div>
    <div class="feature">
      <h3>What we do</h3>
      <div class="icon"><svg width="28" height="28" viewBox="0 0 24 24" fill="#fff"><rect x="5" y="3" width="14" height="18" rx="1"/><path d="M8 12l3 3 5-6" stroke="#1f3a82" stroke-width="2" fill="none"/></svg></div>
      <p>Lorem ipsum dolor sit amet, consectetur adipiscing elit. Sed vitae lacus. Nulla porttitor pellentesque nulla in vehicula. Aliquam erat volutpat. Etiam sollicitudin tellus a molestie.</p>
      <span class="btn">Read more</span>
    </div>
    <div class="feature">
      <h3>How it work</h3>
      <div class="icon"><svg width="28" height="28" viewBox="0 0 24 24" fill="#fff"><circle cx="7" cy="7" r="3"/><circle cx="17" cy="17" r="3"/><path d="M18 4l2 2L6 20l-2-2z"/></svg></div>
      <p>Lorem ipsum dolor sit amet, consectetur adipiscing elit. Sed vitae lacus. Nulla porttitor pellentesque nulla in vehicula. Aliquam erat volutpat. Etiam sollicitudin tellus a molestie.</p>
      <span class="btn">Read more</span>
    </div>
  </section>

  <section class="split">
    <div class="welcome">
      <h2>Welcome to <span>Lorvanix.com</span></h2>
      <p>Lorem ipsum dolor sit amet, consectetur adipiscing elit. Nam vitae tortor ac magna fermentum pretium. Fusce vel metus non lorem pulvinar posuere. Morbi tristique felis at nibh ultricies, in dictum ante viverra. Curabitur ullamcorper mi vel orci rhoncus, eget convallis massa aliquet. Integer malesuada neque non nisl tempus ornare.</p>
      <p>Vivamus dictum quam et risus laoreet, a porta dolor suscipit. Donec tincidunt nibh eu justo feugiat, quis ultrices erat volutpat. Praesent sodales lectus id massa hendrerit, nec posuere odio aliquet. Suspendisse potenti. Aenean vel elit quis augue blandit faucibus. Nunc ut sapien a nunc varius luctus sit amet vitae arcu.</p>
      <p>Pellentesque habitant morbi tristique senectus et netus et malesuada fames ac turpis egestas. Maecenas ultrices velit vel urna mattis, a tempor eros aliquam. Etiam sed dui non libero commodo lobortis.</p>
      <span class="btn">Read more</span>
    </div>
    <aside class="gallery">
      <div class="panel-title">Gallery photos</div>
      <div class="gallery-grid" role="img" aria-label="Nine photos of office teams, servers and technicians">
        <div class="photo"></div><div class="photo"></div><div class="photo"></div>
        <div class="photo"></div><div class="photo"></div><div class="photo"></div>
        <div class="photo"></div><div class="photo"></div><div class="photo"></div>
      </div>
      <div class="view-all">View all</div>
    </aside>
  </section>

  <section class="split" style="margin-top:40px">
    <div class="blog">
      <h3 class="section-title">Recent from the blog</h3>
      <div class="post"><div class="thumb photo" role="img" aria-label="Office team photo"></div><div><h4>Lorem Ipsum Dolor Sit Amet, Consectetur Adipiscing Elit</h4><p>July 18th, 2016</p><p>Sed ut perspiciatis unde omnis iste natus error sit voluptatem accusantium.</p></div></div>
      <div class="post"><div class="thumb photo" role="img" aria-label="Meeting photo"></div><div><h4>Lorem Ipsum Dolor Sit Amet, Consectetur Adipiscing Elit</h4><p>July 12th, 2016</p><p>Sed ut perspiciatis unde omnis iste natus error sit voluptatem accusantium.</p></div></div>
      <div class="post"><div class="thumb photo" role="img" aria-label="Technician photo"></div><div><h4>Lorem Ipsum Dolor Sit Amet, Consectetur Adipiscing Elit</h4><p>July 05th, 2016</p><p>Sed ut perspiciatis unde omnis iste natus error sit voluptatem accusantium.</p></div></div>
      <div class="post"><div class="thumb photo" role="img" aria-label="Workplace photo"></div><div><h4>Lorem Ipsum Dolor Sit Amet, Consectetur Adipiscing Elit</h4><p>June 28th, 2016</p><p>Sed ut perspiciatis unde omnis iste natus error sit voluptatem accusantium.</p></div></div>
      <div class="more">View all</div>
    </div>
    <aside class="events">
      <h3 class="section-title">Latest news &amp; events</h3>
      <div class="event"><div class="thumb photo" role="img" aria-label="Event photo"></div><div><h4>Lorem Ipsum Dolor</h4><p>July 18th, 2016</p><p>Donec pretium felis at velit aliquet dictum.</p></div></div>
      <div class="event"><div class="thumb photo" role="img" aria-label="Event photo"></div><div><h4>Lorem Ipsum Dolor</h4><p>July 10th, 2016</p><p>Donec pretium felis at velit aliquet dictum.</p></div></div>
      <div class="event"><div class="thumb photo" role="img" aria-label="Event photo"></div><div><h4>Lorem Ipsum Dolor</h4><p>July 02nd, 2016</p><p>Donec pretium felis at velit aliquet dictum.</p></div></div>
      <div class="more">View all</div>
    </aside>
  </section>

  <section class="projects">
    <h3 class="section-title">Latest projects</h3>
    <div class="project-row">
      <div class="project"><div class="photo" role="img" aria-label="Office building exterior"></div><h4>Perspiciatis unde omnis</h4><p>Lorem ipsum dolor sit amet</p></div>
      <div class="project"><div class="photo" role="img" aria-label="Team at work in an office"></div><h4>Perspiciatis unde omnis</h4><p>Lorem ipsum dolor sit amet</p></div>
      <div class="project"><div class="photo" role="img" aria-label="Server room corridor"></div><h4>Perspiciatis unde omnis</h4><p>Lorem ipsum dolor sit amet</p></div>
      <div class="project"><div class="photo" role="img" aria-label="Engineer repairing hardware"></div><h4>Perspiciatis unde omnis</h4><p>Lorem ipsum dolor sit amet</p></div>
    </div>
  </section>
</main>

<section class="testimonials">
  <div class="wrap">
    <div class="quote">
      <h3>Testimonials</h3>
      <p>Lorem ipsum dolor sit amet, consectetur adipiscing elit sed diam nonummy euismod tincidunt ut laoreet dolore magna aliquam erat volutpat ut wisi enim ad minim veniam.</p>
      <p class="who">John Smith, Georgia</p>
    </div>
    <div class="newsletter">
      <div class="panel-title">Newsletter</div>
      <p>Subscribe updates about our latest news weekly</p>
      <div class="field"><span>Your email address</span><b>SEND</b></div>
      <div class="check"><i></i>Yes, I agree with terms and conditions</div>
    </div>
  </div>
</section>

<section class="wrap about">
  <div class="photo" role="img" aria-label="Business team around a laptop"></div>
  <div>
    <h2>About Us</h2>
    <p>Lorem ipsum dolor sit amet, consectetur adipiscing elit. Nam vitae tortor ac magna fermentum pretium. Fusce vel metus non lorem pulvinar posuere. Morbi tristique felis at nibh ultricies, in dictum ante viverra. Curabitur ullamcorper mi vel orci rhoncus, eget convallis massa aliquet. Integer malesuada neque non nisl tempus ornare vivamus dictum quam.</p>
    <p>Donec tincidunt nibh eu justo feugiat, quis ultrices erat volutpat. Praesent sodales lectus id massa hendrerit, nec posuere odio aliquet. Suspendisse potenti aenean vel elit quis augue blandit faucibus.</p>
    <span class="btn">Read more</span>
  </div>
</section>

<section class="wrap partners" aria-label="Partners">
  <span></span><span></span><span></span><span></span><span></span><span></span><span></span><span></span>
</section>

<footer class="site-footer">
  <div class="wrap footer-cols">
    <div class="footer-col menu-col">
      <h5>Main menu</h5>
      <ul><li>Home</li><li>About Us</li><li>Services</li><li>News</li><li>Blog</li><li>Testimonials</li><li>Apply</li><li>Latest Projects</li><li>Contact Us</li></ul>
    </div>
    <div class="footer-col links-col">
      <h5>Useful links</h5>
      <ul><li>Sitemap</li><li>FAQ</li><li>Terms of Services</li><li>Privacy Policy</li><li>FAQs</li><li>Affiliates</li><li>Newsletter</li></ul>
    </div>
    <div class="footer-col tweets-col">
      <h5>Latest tweets</h5>
      <div class="tweet"><i></i><span>Nam ut libero quis justo varius tincidunt. Aliquam erat volutpat nunc commodo. 2 hours ago</span></div>
      <div class="tweet"><i></i><span>Nam ut libero quis justo varius tincidunt. Aliquam erat volutpat nunc commodo. 5 hours ago</span></div>
      <div class="tweet"><i></i><span>Nam ut libero quis justo varius tincidunt. Aliquam erat volutpat nunc commodo. 1 day ago</span></div>
      <div class="socials"><span></span><span></span><span></span><span></span></div>
    </div>
    <div class="footer-col contact-col">
      <h5>Contact us</h5>
      <div class="form-row"><label>Name</label><span></span></div>
      <div class="form-row"><label>Email</label><span></span></div>
      <div class="form-row"><label>Phone</label><span></span></div>
      <div class="form-row msg"><label>Message</label><span></span></div>
      <span class="submit">SUBMIT</span>
    </div>
  </div>
  <div class="footer-bar">
    <div class="footer-brand"><i></i><b>Lorvanix</b></div>
    <p class="copyright">Copyright © 2016 Lorvanix.com. All rights reserved.</p>
  </div>
</footer>

</body>
</html>
```